Harborline Network Advisors (HNA) Business Card

Front Side, add Company Logo
1.) Harborline Network Advisors
Director of Operations
Delgado, Marco T
(323) 555 0148
782 n Alder Ave Suite 300 PMB2093
Los Angeles, CA 90013
Marco@HarborlineNA.example
www.HarborlineNA.example
2.) Veteran-Owned Business (with Small EGA)

Back Side
- Pictures are ideas of what you can add. The description is what HNA does.
1.) Business Partners:
- Corvalis Business
- KX&L Business
- Tellmora Business
2.) What we do
- Broker of Internet service (partners above)
- Project Management/ Contract Management
- Government Contracts

```html
<!DOCTYPE html>
<html lang="en">
<head>
<meta charset="utf-8">
<title>Harborline Network Advisors – Business Card</title>
<link rel="stylesheet" href="https://fonts.googleapis.com/css2?family=Arimo:wght@400;700&family=Roboto+Condensed:wght@400;700&display=swap">
<style>
  :root {
    --charcoal: #2b2728;
    --gold: #fbc02d;
    --gold-deep: #f6b91f;
    --ink: #2a2527;
    --white: #ffffff;
    --page: #ececec;
    --photo-dark: #34322f;
    --photo-mid: #4c4f48;
    --photo-green: #2f5a35;
  }
  * { box-sizing: border-box; margin: 0; padding: 0; }
  html, body { width: 1200px; height: 1200px; overflow: hidden; }
  body { background: var(--page); position: relative; font-family: "Arimo", Arial, sans-serif; }

  .card {
    position: absolute; left: 140px; width: 920px; height: 526px;
    border-radius: 28px; overflow: hidden;
  }
  .card--front { top: 40px; background: var(--gold); }
  .card--back { top: 630px; }

  /* front */
  .brand-panel {
    position: absolute; left: 0; top: 0; width: 465px; height: 356px;
    background: var(--charcoal);
    display: flex; align-items: center; justify-content: center; gap: 14px;
  }
  .brand-mark { width: 22px; height: 22px; border-radius: 50%; background: var(--gold); flex: none; }
  .brand-name {
    font-family: "Roboto Condensed", Arial, sans-serif; font-weight: 700;
    color: var(--gold); font-size: 30px; line-height: 1.15; text-transform: uppercase;
    letter-spacing: 1px; width: 250px;
  }

  .contact { position: absolute; left: 510px; top: 68px; color: var(--ink); }
  .contact__name {
    font-family: "Roboto Condensed", Arial, sans-serif; font-weight: 700;
    font-size: 40px; line-height: 1; text-transform: uppercase;
  }
  .contact__title { font-size: 20px; margin-top: 4px; }
  .contact__address { font-size: 21px; line-height: 27px; margin-top: 14px; margin-left: 2px; }
  .contact__list { list-style: none; margin-top: 10px; font-size: 21px; line-height: 28px; }
  .contact__list li { display: flex; align-items: center; gap: 18px; }
  .contact__list svg { width: 20px; height: 20px; flex: none; fill: var(--ink); }

  .partner-band {
    position: absolute; left: 0; top: 356px; width: 100%; height: 89px;
    background: var(--white); display: flex; align-items: center;
  }
  .partner {
    flex: 1; text-align: center; font-size: 22px; font-weight: 700; color: var(--ink);
  }

  .veteran-band {
    position: absolute; left: 0; top: 445px; width: 465px; height: 81px;
    background: var(--charcoal); display: flex; align-items: center; padding-left: 86px; gap: 14px;
  }
  .veteran-badge { width: 40px; height: 40px; border-radius: 50%; background: #8d8a86; flex: none; }
  .veteran-text {
    font-family: "Roboto Condensed", Arial, sans-serif; color: var(--white);
    font-size: 22px; text-transform: uppercase;
  }

  /* back */
  .back-photo {
    position: absolute; inset: 0;
    background: linear-gradient(160deg, var(--photo-mid) 0%, var(--photo-dark) 45%, var(--photo-green) 70%, var(--photo-dark) 100%);
  }
  .back-brand {
    position: absolute; left: 0; top: 0; width: 100%; height: 431px;
    display: flex; align-items: center; justify-content: center; gap: 16px;
  }
  .back-brand .brand-name { font-size: 34px; width: 290px; }
  .services-band {
    position: absolute; left: 0; top: 431px; width: 100%; height: 44px;
    background: var(--gold); display: flex; align-items: center; justify-content: center;
    font-family: "Roboto Condensed", Arial, sans-serif; font-size: 21px; color: var(--ink);
    white-space: nowrap;
  }
  .services-band .sep { margin: 0 10px; }
</style>
</head>
<body>

<section class="card card--front">
  <div class="brand-panel">
    <span class="brand-mark"></span>
    <span class="brand-name">Harborline Network Advisors</span>
  </div>

  <div class="contact">
    <h1 class="contact__name">Delgado, Marco T</h1>
    <p class="contact__title">Director of Operations</p>
    <p class="contact__address">782 n Alder Ave, Suite 300<br>PMB2093<br>Los Angeles, CA 90013</p>
    <ul class="contact__list">
      <li><svg viewBox="0 0 24 24"><path d="M6.6 10.8a15.1 15.1 0 0 0 6.6 6.6l2.2-2.2c.3-.3.7-.4 1-.2 1.1.4 2.3.6 3.6.6.6 0 1 .4 1 1V20c0 .6-.4 1-1 1A17 17 0 0 1 3 4c0-.6.4-1 1-1h3.5c.6 0 1 .4 1 1 0 1.3.2 2.5.6 3.6.1.3 0 .7-.2 1z"/></svg>(323) 555 0148</li>
      <li><svg viewBox="0 0 24 24"><path d="M2 5h20v14H2z M2 5l10 8 10-8" fill="none" stroke="#2a2527" stroke-width="2.4"/></svg>Marco@HarborlineNA.example</li>
      <li><svg viewBox="0 0 24 24"><circle cx="12" cy="12" r="9" fill="none" stroke="#2a2527" stroke-width="2.4"/><path d="M3 12h18M12 3c3 3 3 15 0 18M12 3c-3 3-3 15 0 18" fill="none" stroke="#2a2527" stroke-width="1.6"/></svg>www.HarborlineNA.example</li>
    </ul>
  </div>

  <div class="partner-band">
    <span class="partner">KX&amp;L Business</span>
    <span class="partner">Corvalis Business</span>
    <span class="partner">Tellmora Business</span>
  </div>

  <div class="veteran-band">
    <span class="veteran-badge"></span>
    <span class="veteran-text">Veteran-Owned Business</span>
  </div>
</section>

<section class="card card--back">
  <div class="back-photo" role="img" aria-label="Close-up photo of a fiber patch panel with green connectors and a red cable"></div>
  <div class="back-brand">
    <span class="brand-mark"></span>
    <span class="brand-name">Harborline Network Advisors</span>
  </div>
  <div class="services-band">
    Broker of Internet service<span class="sep">|</span>Project Management/ Contract Management<span class="sep">|</span>Government Contracts
  </div>
</section>

</body>
</html>
```